Need webdesign for service company that provides Car hiring service and transit service

We need a web design for a company that provides airport transit services and transport services including Limo, Corporate cars, Disability transit, Family transit service. We need is a simple and professional design.

Below is site which we like and also offer the same service http://www.ridevelto.com.au/

Reason: Waiting for the Feedback from multiple stakeholders. Need the time to select and approve the design

Target Market(s)

Tourism, Travel

Industry/Entity Type

Airport

Number of Pages Required

3 page

Font styles to use
Decorative
Script

Requirements
Must have
• Simple and Professional, Site we like http://www.ridevelto.com.au/ and also need to mobile friendly
Should not have
• Shouldn't have too many images

```html
<!DOCTYPE html>
<html lang="en">
<head>
<meta charset="utf-8">
<title>Rovanta – Private &amp; Business Transport</title>
<link href="https://fonts.googleapis.com/css2?family=Jost:ital,wght@0,300;0,400;0,500;0,700;1,300&family=Lato:wght@400;700&display=swap" rel="stylesheet">
<style>
:root{
  --page:#f3f8f8;
  --ink:#1c1c1e;
  --gold:#c9a35a;
  --gold-soft:#efc75e;
  --maroon:#8a3a35;
  --panel:rgba(226,222,209,0.94);
  --line:#6f6a60;
  --muted:#8b857a;
  --footer:#48464b;
  --footer-text:#f2f2f2;
}
*{margin:0;padding:0;box-sizing:border-box}
html,body{width:829px;height:1200px;overflow:hidden}
body{position:relative;background:var(--page);font-family:'Jost',sans-serif;color:var(--ink)}
.hero{position:absolute;left:0;top:0;width:829px;height:462px;
  background:radial-gradient(circle at 30% 20%,#fff6d9 0%,rgba(255,246,217,0) 45%),
  linear-gradient(100deg,#d9b46a 0%,#f3e4bd 25%,#fbf6ea 45%,#c8a078 65%,#e8d2b4 85%,#f6efe2 100%)}
.brand{position:absolute;left:70px;top:18px;display:flex;align-items:center;gap:8px;
  font-family:'Jost',sans-serif;font-weight:500;font-size:21px;color:var(--ink);letter-spacing:0.5px}
.brand-mark{width:26px;height:26px;border-radius:50%;background:var(--ink)}
.top-icons{position:absolute;top:18px;left:644px;display:flex;gap:16px;align-items:center}
.headline{position:absolute;left:109px;top:142px;font-weight:700;font-size:46px;letter-spacing:6px;color:var(--gold-soft);opacity:.85;white-space:nowrap}
.tagline{position:absolute;left:109px;top:204px;font-size:14px;letter-spacing:4.4px;color:#3a2e24;white-space:nowrap}
.quote{position:absolute;left:120px;top:366px;width:590px;height:241px;background:var(--panel)}
.quote-title{position:absolute;left:46px;top:28px;font-size:21px;letter-spacing:4.5px;font-weight:400;white-space:nowrap}
.quote-title b{font-weight:700}
.field-label{position:absolute;left:46px;width:181px;height:30px;border-bottom:1px solid var(--line);
  display:flex;align-items:center;font-size:15px;letter-spacing:4px;font-weight:500;white-space:nowrap}
.field-label svg{margin:0 8px 0 6px;flex:none}
.field-input{position:absolute;left:242px;width:296px;height:30px;border-bottom:1px solid var(--line);
  font-style:italic;font-weight:300;font-size:17px;color:var(--muted);letter-spacing:1.4px;padding-left:10px;display:flex;align-items:center;white-space:nowrap}
.add-stops{position:absolute;left:46px;top:180px;display:flex;align-items:center;gap:12px;font-size:15px;letter-spacing:4.5px;color:var(--maroon);white-space:nowrap}
.fare-btn{position:absolute;left:242px;top:171px;width:296px;height:38px;background:var(--gold);color:#fff;
  font-size:15px;letter-spacing:4.5px;display:flex;align-items:center;justify-content:center;white-space:nowrap}
.section-title{position:absolute;left:0;width:829px;top:648px;text-align:center;font-size:24px;letter-spacing:3px;font-weight:400;white-space:nowrap}
.dots{position:absolute;left:391px;top:695px}
.services{position:absolute;left:54px;top:737px;width:717px;height:242px;display:flex}
.service{position:relative;width:50%;height:100%}
.service.airport{background:linear-gradient(120deg,#e9e1d8 0%,#b7a08a 45%,#3f3a38 80%,#d8cfc6 100%)}
.service.transport{background:linear-gradient(110deg,#6b3a22 0%,#c8a57e 40%,#e9dccb 60%,#4a2414 100%)}
.service-label{position:absolute;top:148px;left:46px;width:267px;height:61px;background:rgba(240,236,232,0.82);padding:9px}
.service-label span{display:flex;height:100%;border:1px solid #6a635d;align-items:center;justify-content:center;
  font-size:14px;letter-spacing:1.3px;color:#3a332e;white-space:nowrap}
.footer{position:absolute;left:0;top:1046px;width:829px;height:154px;background:var(--footer);color:var(--footer-text);font-family:'Lato',sans-serif}
.footer-info{position:absolute;left:54px;top:23px;font-size:10px}
.footer-links{display:flex;gap:11px;margin-top:5px;font-size:8px;white-space:nowrap}
.footer-links .gap{margin-left:10px}
.footer-contact{position:absolute;right:58px;top:27px;text-align:right;font-size:8.5px;line-height:15px;font-weight:700;white-space:nowrap}
.footer-contact .addr-title{margin-top:10px;font-size:10.5px;font-weight:400}
.social{position:absolute;left:661px;top:1157px;display:flex;gap:11px}
.social i{display:block;width:20px;height:20px;border-radius:50%;border:1px solid #8d8b90}
</style>
</head>
<body>
<header class="hero" role="img" aria-label="Photo of a smiling couple in sunglasses, the man pointing ahead on a sunny street"></header>
<div class="brand"><span class="brand-mark"></span>ROVANTA</div>
<nav class="top-icons">
  <svg width="20" height="22" viewBox="0 0 20 22" aria-label="Call"><path d="M4 2 L8 2 L9 7 L6.5 8.5 Q8 13 12 15.5 L13.5 13 L18 14 L18 18 Q17 20 14 19.5 Q4 16 2 5 Q2 2.5 4 2 Z" fill="#4a4a4a"/></svg>
  <svg width="22" height="22" viewBox="0 0 22 22" aria-label="Search"><circle cx="9" cy="9" r="7" fill="none" stroke="#4a4a4a" stroke-width="2"/><line x1="14" y1="14" x2="20" y2="20" stroke="#4a4a4a" stroke-width="2.4"/></svg>
  <svg width="34" height="20" viewBox="0 0 34 20" aria-label="Menu"><rect x="0" y="1" width="34" height="2.4" fill="#333"/><rect x="0" y="8.5" width="34" height="2.4" fill="#333"/><rect x="0" y="16" width="34" height="2.4" fill="#333"/></svg>
</nav>
<h1 class="headline">PRIVATE &amp; BUSSINESS</h1>
<p class="tagline">PERSONALISED TRANSPORT SERVICE</p>

<section class="quote">
  <h2 class="quote-title"><b>INSTANT</b> QUOTE</h2>
  <div class="field-label" style="top:65px"><svg width="18" height="16" viewBox="0 0 18 16"><circle cx="5" cy="8" r="4" fill="none" stroke="#333"/><line x1="15" y1="1" x2="15" y2="15" stroke="#333"/></svg>ORIGIN</div>
  <div class="field-input" style="top:65px">Public locations or exact address</div>
  <div class="field-label" style="top:111px"><svg width="18" height="18" viewBox="0 0 18 18"><path d="M5 16 Q0 9 0.8 6 A4.3 4.3 0 0 1 9.2 6 Q10 9 5 16 Z" fill="none" stroke="#333"/><circle cx="5" cy="6" r="1.6" fill="none" stroke="#333"/><line x1="15" y1="1" x2="15" y2="17" stroke="#333"/></svg>DESTINATION</div>
  <div class="field-input" style="top:111px">Public locations or exact address</div>
  <div class="add-stops"><svg width="20" height="20" viewBox="0 0 20 20"><line x1="10" y1="0" x2="10" y2="20" stroke="#555"/><line x1="0" y1="10" x2="20" y2="10" stroke="#555"/></svg>ADD STOPS</div>
  <div class="fare-btn">ESTIMATE FARE</div>
</section>

<h2 class="section-title">LOREM IPSUM DOLOR SIT AMET CONSECTETUR</h2>
<svg class="dots" width="48" height="8" viewBox="0 0 48 8"><g fill="none" stroke="#666" stroke-width="0.8"><path d="M3 2 L5 4 L3 6 L1 4Z"/><path d="M13 2 L15 4 L13 6 L11 4Z"/><path d="M35 2 L37 4 L35 6 L33 4Z"/><path d="M45 2 L47 4 L45 6 L43 4Z"/></g><path d="M24 1 L27 4 L24 7 L21 4Z" fill="#111"/></svg>

<section class="services">
  <div class="service airport" role="img" aria-label="Photo of a business couple smiling and looking at travel documents">
    <div class="service-label"><span>AIRPORT TRANSIT SERVICES</span></div>
  </div>
  <div class="service transport" role="img" aria-label="Photo of a gloved chauffeur opening a car door">
    <div class="service-label" style="left:45px"><span>TRANSPORTATION SERVICES</span></div>
  </div>
</section>

<footer class="footer">
  <div class="footer-info">
    Information
    <div class="footer-links"><span>About us</span><span>Online enquiry</span><span>Call us</span><span class="gap">General enquiries</span><span>Privacy policy</span><span>Refund policy</span></div>
  </div>
  <div class="footer-contact">
    Phone: +91-80-40000000<br>Email: hello@rovanta.co
    <div class="addr-title">Address</div>
    Lorem ipsum Dolor sit amet, consectetur Elit - 400400, Eiusmod Tempor
  </div>
</footer>
<div class="social" aria-label="Social links"><i></i><i></i><i></i><i></i></div>
</body>
</html>
```